La etiqueta deberá contener lo siguiente:
-Titulo: Miel de Agave Kosher
-Logo de DOVRA (realizado por ustedes, adjunto diseño)
-Logo del certificado: KOSHER (Se adjuntan certificado)
-Mililitros: 750 ml
-Información nutrimental: se adjunta tabla
La miel deberá sobresalir de las demás por el estilo lujoso y llamativo de la etiqueta.

```html
<!DOCTYPE html>
<html lang="es">
<head>
<meta charset="UTF-8">
<title>DOVRA – Miel de Agave Kosher, etiqueta</title>
<link href="https://fonts.googleapis.com/css2?family=Barlow+Condensed:wght@400;500;600;700&display=swap" rel="stylesheet">
<style>
  :root {
    --bg: #efefef;
    --label-black: #050505;
    --gold: #d9b440;
    --gold-light: #f2d866;
    --gold-deep: #b8902a;
    --text-light: #e8e8e8;
  }
  * { margin: 0; padding: 0; box-sizing: border-box; }
  html, body { width: 1200px; height: 1058px; overflow: hidden; }
  body {
    background: var(--bg);
    font-family: "Barlow Condensed", "Arial Narrow", sans-serif;
    position: relative;
  }
  .label {
    position: absolute;
    top: 250px;
    width: 500px;
    height: 560px;
    background: var(--label-black);
    overflow: hidden;
  }
  .label--front { left: 60px; }
  .label--back { left: 640px; }

  .honeycomb-band {
    position: absolute;
    left: 0; top: 0;
    width: 100%;
    height: 130px;
    background: linear-gradient(100deg, var(--gold-deep) 0%, var(--gold-light) 35%, var(--gold) 60%, var(--gold-light) 85%, var(--gold-deep) 100%);
    opacity: .92;
  }

  .brand {
    position: absolute;
    top: 215px;
    width: 100%;
    display: flex;
    align-items: center;
    justify-content: center;
    gap: 12px;
  }
  .brand__mark {
    width: 14px; height: 14px;
    border-radius: 50%;
    background: var(--gold);
  }
  .brand__name {
    font-weight: 500;
    font-size: 34px;
    letter-spacing: 6px;
    color: var(--text-light);
  }

  .product-title {
    position: absolute;
    top: 318px;
    width: 100%;
    text-align: center;
    font-weight: 400;
    font-size: 58px;
    letter-spacing: 2px;
    color: var(--gold);
    line-height: 1;
  }
  .product-subtitle {
    position: absolute;
    top: 388px;
    width: 100%;
    text-align: center;
    font-weight: 400;
    font-size: 32px;
    letter-spacing: 6px;
    color: var(--text-light);
  }
  .volume {
    position: absolute;
    top: 495px;
    width: 100%;
    text-align: center;
    font-weight: 700;
    font-size: 28px;
    color: var(--gold);
  }

  .nutrition {
    position: absolute;
    left: 135px;
    top: 62px;
    width: 230px;
    height: 322px;
    border: 3px solid var(--gold);
    border-radius: 16px;
    padding: 18px 14px 10px;
    color: var(--gold);
  }
  .nutrition__title {
    text-align: center;
    font-weight: 700;
    font-size: 19px;
    line-height: 1.05;
    letter-spacing: .5px;
    margin-bottom: 12px;
  }
  .nutrition__row {
    display: flex;
    justify-content: space-between;
    font-size: 8.5px;
    line-height: 1.35;
    padding: 1px 0;
  }
  .nutrition__row--bold { font-weight: 700; }
  .nutrition__row--indent span:first-child { padding-left: 22px; }
  .nutrition__rule { border-top: 1px solid var(--gold); margin: 2px 0; }
  .nutrition__rule--thick { border-top: 3px solid var(--gold); margin: 4px 0; }
  .value-stack { text-align: right; }

  .cert-seal {
    position: absolute;
    left: 210px;
    top: 445px;
    width: 80px; height: 80px;
    border-radius: 50%;
    background: radial-gradient(circle, var(--gold) 0%, var(--gold-deep) 100%);
  }
</style>
</head>
<body>
  <section class="label label--front">
    <div class="honeycomb-band" role="img" aria-label="Patrón decorativo de panal en tonos dorados"></div>
    <div class="brand">
      <span class="brand__mark"></span>
      <span class="brand__name">DOVRA</span>
    </div>
    <h1 class="product-title">MIEL DE AGAVE</h1>
    <p class="product-subtitle">KOSHER</p>
    <p class="volume">750ml</p>
  </section>

  <section class="label label--back">
    <div class="nutrition">
      <h2 class="nutrition__title">DECLARACIÓN<br>NUTRIMENTAL</h2>
      <div class="nutrition__row"><span>Contenido energético por envase</span><span class="value-stack">2,050 kcal<br>8,639 kJ</span></div>
      <div class="nutrition__rule nutrition__rule--thick"></div>
      <div class="nutrition__row"><span>Tamaño de la porción</span><span>100g</span></div>
      <div class="nutrition__row"><span>Porciones por envase</span><span>3.3</span></div>
      <div class="nutrition__row nutrition__row--bold"><span>Contenido energético por porción</span><span class="value-stack">310 kcal<br>1,309 kJ</span></div>
      <div class="nutrition__rule nutrition__rule--thick"></div>
      <div class="nutrition__row nutrition__row--bold"><span>Proteínas</span><span>0 g</span></div>
      <div class="nutrition__rule"></div>
      <div class="nutrition__row"><span>Grasas</span><span>0 g</span></div>
      <div class="nutrition__row nutrition__row--bold nutrition__row--indent"><span>Grasa saturada</span><span>0 mg</span></div>
      <div class="nutrition__rule"></div>
      <div class="nutrition__row nutrition__row--bold nutrition__row--indent"><span>Grasas trans</span><span>0 mg</span></div>
      <div class="nutrition__rule"></div>
      <div class="nutrition__row"><span>Hidratos de carbono disponibles</span><span>77 g</span></div>
      <div class="nutrition__row nutrition__row--indent"><span>Azúcares</span><span>77 g</span></div>
      <div class="nutrition__row nutrition__row--bold nutrition__row--indent"><span>Azúcares añadidos</span><span>0 g</span></div>
      <div class="nutrition__rule"></div>
      <div class="nutrition__row"><span>Fibra dietética</span><span>menos de 1 g</span></div>
      <div class="nutrition__rule"></div>
      <div class="nutrition__row nutrition__row--bold"><span>Sodio</span><span>0 mg</span></div>
    </div>
    <div class="cert-seal" role="img" aria-label="Sello de certificación kosher"></div>
  </section>
</body>
</html>
```